Business card design for event company

need design double sided in square shape ( approx 6x6cm) in matt grey shades
front side :
logo ( could be in one color like picture attached ) printpress effect in a rect box

back side :
name in big font with silver foil finish ( similar to attached pic )

phone number i would like to see how it will look like if embossed ( like in credit cards )

Sample for contact on card ( will need 5 different contacts) - pls. include small icons next to each contact

WALEED RAFIQI
Managing Director

+971 50 317 6490
waleed@loomcrestuae.com
www.loomcrest.ae
Building C2 , Office 713
Dubai Saffron Heights

Please consider this is an urgent project . thank you in advance

```html
<!DOCTYPE html>
<html lang="en">
<head>
<meta charset="utf-8">
<title>Loomcrest Business Card</title>
<link href="https://fonts.googleapis.com/css2?family=Roboto:wght@500&family=Work+Sans:wght@400;500&display=swap" rel="stylesheet">
<style>
  :root {
    --page-bg: #dedede;
    --card-bg: #252525;
    --card-bg-deep: #1c1c1c;
    --silver: #c8c8c8;
    --silver-soft: #a9a9a9;
    --silver-bright: #e2e2e2;
  }
  * { margin: 0; padding: 0; box-sizing: border-box; }
  html, body {
    width: 1200px;
    height: 897px;
    overflow: hidden;
    background: var(--page-bg);
  }
  .canvas {
    position: relative;
    width: 1200px;
    height: 897px;
  }
  .card {
    position: absolute;
    top: 190px;
    width: 515px;
    height: 512px;
    background: linear-gradient(160deg, var(--card-bg) 0%, var(--card-bg-deep) 100%);
    color: var(--silver);
    font-family: "Work Sans", sans-serif;
  }
  .card--contact { left: 59px; }
  .card--brand { left: 626px; }

  .brand-name {
    position: absolute;
    font-family: "Work Sans", sans-serif;
    font-weight: 400;
    color: var(--silver);
    white-space: nowrap;
    line-height: 1;
  }
  .card--contact .brand-name {
    top: 42px;
    right: 40px;
    font-size: 34px;
  }
  .card--brand .brand-name {
    top: 50%;
    left: 50%;
    transform: translate(-50%, -50%);
    font-size: 60px;
  }

  .holder {
    position: absolute;
    left: 37px;
    top: 283px;
  }
  .holder-name {
    font-family: "Roboto", sans-serif;
    font-weight: 500;
    font-size: 27px;
    letter-spacing: 0.2px;
    color: var(--silver-bright);
    line-height: 1.1;
  }
  .holder-role {
    font-size: 15.5px;
    color: var(--silver-soft);
    letter-spacing: 0.6px;
    margin-top: 4px;
  }

  .contact-list {
    position: absolute;
    left: 37px;
    top: 344px;
    list-style: none;
  }
  .contact-item {
    display: flex;
    align-items: center;
    height: 22px;
    font-size: 16px;
    letter-spacing: 0.5px;
    color: var(--silver);
  }
  .contact-item svg {
    width: 11px;
    height: 11px;
    margin-right: 11px;
    flex: none;
  }
  .contact-item--phone { color: var(--silver-soft); letter-spacing: 1px; }

  .address {
    position: absolute;
    left: 37px;
    top: 432px;
    font-size: 16px;
    line-height: 22px;
    letter-spacing: 0.6px;
    color: var(--silver-soft);
    font-style: normal;
  }
</style>
</head>
<body>
<main class="canvas">
  <section class="card card--contact" aria-label="Card back with contact details">
    <div class="brand-name">Loomcrest</div>

    <div class="holder">
      <h1 class="holder-name">WALEED RAFIQI</h1>
      <p class="holder-role">Managing Director</p>
    </div>

    <ul class="contact-list">
      <li class="contact-item contact-item--phone">
        <svg viewBox="0 0 12 12" aria-hidden="true"><path d="M2.5 1 L4.3 1 L5 3.3 L3.9 4.2 C4.5 5.6 5.7 6.9 7.2 7.6 L8.1 6.6 L10.5 7.4 L10.5 9.3 C10.5 10 9.9 10.5 9.2 10.4 C5 10 1.7 6.6 1.4 2.3 C1.4 1.6 1.8 1 2.5 1 Z" fill="currentColor"/></svg>
        +971 50 317 6490
      </li>
      <li class="contact-item">
        <svg viewBox="0 0 12 12" aria-hidden="true"><rect x="1" y="2.5" width="10" height="7" fill="none" stroke="currentColor" stroke-width="1.2"/><path d="M1.3 3 L6 6.6 L10.7 3" fill="none" stroke="currentColor" stroke-width="1.2"/></svg>
        waleed@loomcrestuae.com
      </li>
      <li class="contact-item">
        <svg viewBox="0 0 12 12" aria-hidden="true"><circle cx="6" cy="6" r="4.8" fill="none" stroke="currentColor" stroke-width="1.1"/><ellipse cx="6" cy="6" rx="2.1" ry="4.8" fill="none" stroke="currentColor" stroke-width="1"/><path d="M1.2 6 H10.8 M2 3.6 H10 M2 8.4 H10" stroke="currentColor" stroke-width="0.9"/></svg>
        www.loomcrest.ae
      </li>
    </ul>

    <address class="address">
      Building C2 , Office 713<br>
      Dubai Saffron Heights
    </address>
  </section>

  <section class="card card--brand" aria-label="Card front with company name">
    <div class="brand-name">Loomcrest</div>
  </section>
</main>
</body>
</html>
```